Visitenkarten für Erstellung von Beleihungswert- und Verkehrswertgutachten.
Zielgruppe
Ich erstelle Beleihungswert- und Verkehrswertgutachten.
Meine Zielgruppe sind alle Immobilieneigentümer, Kaufinteressenten, Erben von Immobilienvermögen evtl. auch Anwälte, Steuerberater.
Aufgabenstellung
Der Fokus liegt auf der Wertermittlung von Immobilien

```html
<!DOCTYPE html>
<html lang="de">
<head>
<meta charset="utf-8">
<title>Visitenkarte Lomisar Dreva</title>
<link href="https://fonts.googleapis.com/css2?family=Alegreya:wght@500;700;800&display=swap" rel="stylesheet">
<style>
  :root {
    --page: #ffffff;
    --card: #060504;
    --card-glow: #1a1309;
    --gold: #dca94c;
    --gold-light: #f3cf7a;
    --gold-deep: #b8832d;
  }
  html, body {
    margin: 0;
    padding: 0;
    width: 1178px;
    height: 1200px;
    overflow: hidden;
    background: var(--page);
  }
  body {
    position: relative;
    font-family: "Alegreya", Georgia, serif;
    color: var(--gold);
  }
  .card {
    position: absolute;
    width: 788px;
    height: 510px;
    box-shadow: 0 4px 22px rgba(0,0,0,0.55);
    overflow: hidden;
  }
  .card-front { left: 199px; top: 49px; }
  .card-back { left: 195px; top: 640px; }
  .city-texture {
    position: absolute;
    inset: 0;
    background: radial-gradient(ellipse at 50% 40%, var(--card-glow) 0%, var(--card) 75%);
  }
  .brand {
    position: absolute;
    left: 0; right: 0;
    top: 225px;
    text-align: center;
    font-weight: 700;
    font-size: 44px;
    letter-spacing: 4px;
    color: var(--gold);
  }
  .holder-name {
    position: absolute;
    left: 0; right: 0;
    top: 28px;
    text-align: center;
    font-weight: 800;
    font-size: 58px;
    line-height: 1;
    background: linear-gradient(180deg, var(--gold-light), var(--gold-deep));
    -webkit-background-clip: text;
    background-clip: text;
    color: transparent;
  }
  .name-rule {
    position: absolute;
    left: 263px;
    top: 102px;
    width: 263px;
    height: 2px;
    background: var(--gold);
  }
  .name-rule::before {
    content: "";
    position: absolute;
    left: 0; top: -1px;
    width: 45px; height: 4px;
    background: var(--gold);
  }
  .qualifications {
    position: absolute;
    left: 100px; right: 100px;
    top: 168px;
    margin: 0;
    text-align: center;
    font-weight: 700;
    font-size: 19px;
    line-height: 25.5px;
    color: var(--gold);
  }
  .contact {
    position: absolute;
    display: flex;
    align-items: center;
    gap: 14px;
    font-weight: 700;
    font-size: 24px;
    color: var(--gold);
  }
  .contact-mail { left: 126px; top: 366px; }
  .contact-phone { left: 479px; top: 368px; }
  .icon-box {
    width: 34px; height: 34px;
    border: 2px solid var(--gold);
    display: flex; align-items: center; justify-content: center;
  }
  .icon-box svg { width: 18px; height: 18px; fill: var(--gold); }
  .location-icon {
    position: absolute;
    left: 376px; top: 422px;
  }
  .address {
    position: absolute;
    left: 0; right: 0;
    top: 465px;
    text-align: center;
    font-weight: 700;
    font-size: 24px;
    color: var(--gold);
  }
</style>
</head>
<body>
  <section class="card card-front">
    <div class="city-texture" role="img" aria-label="Dunkles Muster aus beleuchteten Hochhausfenstern"></div>
    <div class="brand">LOMISAR DREVA</div>
  </section>

  <section class="card card-back">
    <div class="city-texture" role="img" aria-label="Dunkles Muster aus beleuchteten Hochhausfenstern"></div>
    <h1 class="holder-name" style="margin:0">Lomisar Dreva</h1>
    <div class="name-rule"></div>
    <p class="qualifications">
      DIN ISO/IEC 17024 zertifizierte Bau-Sachverständige für die<br>
      Markt- und Beleihungswertermittlung von Wohn- und<br>
      Gewerbeimmobilie<br>
      PRÜFKOR D1,D3 und D3 zertifiziert<br>
      SIGEKO = Sicherheits- und Gesundheitsschutz-Koordinator für<br>
      Baustellen.
    </p>
    <div class="contact contact-mail">
      <span class="icon-box"><svg viewBox="0 0 20 20"><path d="M2 5h16v10H2z" fill="none" stroke="currentColor"/><path d="M2 5h16v10H2V5zm1.5 1.2L10 11l6.5-4.8V14h-13V6.2z"/></svg></span>
      <span>l.dreva@postfeld.de</span>
    </div>
    <div class="contact contact-phone">
      <span class="icon-box"><svg viewBox="0 0 20 20"><path d="M5 2.5l3 3-1.6 2.2c.9 2 2.4 3.5 4.4 4.4L13 10.5l3 3-2 3C8.5 16 4 11.5 3.5 5z"/></svg></span>
      <span>+ 49 176 ........</span>
    </div>
    <div class="location-icon icon-box"><svg viewBox="0 0 20 20"><path d="M10 1.5a5.5 5.5 0 0 0-5.5 5.5c0 4 5.5 11 5.5 11s5.5-7 5.5-11A5.5 5.5 0 0 0 10 1.5zm0 7.8a2.3 2.3 0 1 1 0-4.6 2.3 2.3 0 0 1 0 4.6z"/></svg></div>
    <div class="address">Lindenhof-Weg 4/2, 70599 Talbach</div>
  </section>
</body>
</html>
```